Redesign - Trifold Brochure - Adding new and fresh look.

I have attached what we currently have as a brochure but we need it to be redesigned. The information content is accurate but looking for fresh new design/layout. Please see the images attached. In tif and pdf format. If you need a different format to work please specify and will do my best to upload it.

Target Market(s)

Retail giveaways to educate customers.

Requirements
Must have
• New fresh look

```html
<!DOCTYPE html>
<html lang="en">
<head>
<meta charset="utf-8">
<title>How Does CBD Work In Your Body? — Brochure Panel</title>
<link rel="stylesheet" href="https://fonts.googleapis.com/css2?family=Oswald:wght@600;700&family=Open+Sans:ital,wght@0,400;0,600;0,700;1,700&display=swap">
<style>
:root{
  --orange:#f39a1e;
  --orange-light:#f8b62b;
  --green:#8bbf3f;
  --lime:#cfdc2c;
  --text:#555a5e;
  --text-dark:#444;
  --panel-dark:#0e1a1d;
  --white:#fff;
}
*{margin:0;padding:0;box-sizing:border-box}
html,body{width:1200px;height:933px;overflow:hidden;background:var(--white)}
body{position:relative;font-family:"Open Sans",Arial,sans-serif;color:var(--text)}
.abs{position:absolute}
.photo-frame{left:42px;top:44px;width:316px;height:283px;border:3px dashed #555;border-right:none;border-bottom:none}
.photo-frame::after{content:"";position:absolute}
.photo{left:57px;top:57px;width:314px;height:256px;background:linear-gradient(135deg,#7a3a12 0%,#c97a1a 35%,#f0b43c 55%,#8a5a2a 80%,#3d4a2a 100%)}
.photo-band{left:57px;top:312px;width:314px;height:29px;background:var(--green)}
.pointer{left:85px;top:340px}
.frame-corner{left:42px;top:300px;width:12px;height:27px;border-left:3px dashed #555;border-bottom:3px solid #555}
.heading{font-family:"Oswald",Impact,sans-serif;font-weight:700;color:var(--orange)}
.what-title{left:46px;top:384px;font-size:40px;line-height:50px}
.what-text{left:46px;top:450px;width:328px;font-size:13px;line-height:16.2px;text-align:justify}
.what-text em{font-weight:700}
.what-text strong{font-weight:700;color:var(--text-dark)}
.uses{left:50px;top:592px;list-style:none}
.uses li{font-size:15.5px;font-weight:600;color:var(--text);line-height:29.4px;padding-left:21px;position:relative}
.uses li::before{content:"";position:absolute;left:0;top:12px;width:6px;height:6px;border-radius:50%;background:var(--green)}
.sq-lime{left:28px;top:780px;width:53px;height:53px;background:var(--lime)}
.sq-orange{left:0;top:850px;width:75px;height:83px;background:var(--orange)}
.sq-green{left:91px;top:850px;width:54px;height:53px;background:var(--green)}
.title-bar{left:408px;top:42px;width:792px;height:58px;background:linear-gradient(90deg,var(--orange),var(--orange-light));display:flex;align-items:center;justify-content:center}
.title-bar h1{font-family:"Oswald",Impact,sans-serif;font-weight:700;color:var(--white);font-size:39px;letter-spacing:.3px;padding-left:0}
.intro{left:440px;top:111px;width:712px;font-size:13px;line-height:16.3px;text-align:justify}
.benefits{left:408px;top:255px;width:792px;text-align:center;font-size:16px;font-weight:700;font-style:italic;color:var(--orange)}
.tag{height:19px;width:80px;color:var(--white);font-size:13px;font-weight:700;display:flex;align-items:center;justify-content:center}
.tag-high{left:476px;top:307px;background:var(--orange)}
.tag-low{left:848px;top:307px;background:var(--green)}
.facts{font-size:13px;font-weight:600;line-height:16px;color:var(--text)}
.facts-high{left:578px;top:307px}
.facts-low{left:945px;top:307px}
.visual{left:440px;top:399px;width:712px;height:477px;background:radial-gradient(ellipse at 82% 55%,#c8401a 0%,#8a2a14 25%,#2a2a28 55%,transparent 75%),radial-gradient(ellipse at 18% 50%,#1f6f7a 0%,#123a44 40%,transparent 70%),var(--panel-dark)}
.connectors{left:440px;top:399px}
.receptor-box{left:657px;top:420px;width:132px;height:437px;background:#0b0f10;border:2px solid var(--white);border-radius:9px;padding:6px 12px 0}
.receptor-box p{color:#e8e8e8;font-size:10.3px;line-height:13px;text-align:justify;padding:12px 0 10px;border-bottom:1px solid #cfcfcf}
.receptor-box p:first-child{padding-top:20px}
.receptor-box p:last-child{border-bottom:none;padding-top:14px}
.bottom-bar{left:408px;top:888px;width:792px;height:45px;background:linear-gradient(90deg,var(--orange),var(--orange-light))}
</style>
</head>
<body>
  <div class="abs photo-frame"></div>
  <div class="abs photo" role="img" aria-label="Close-up of amber CBD oil dripping from a dropper into a glass bottle"></div>
  <div class="abs photo-band"></div>
  <svg class="abs pointer" width="58" height="26" viewBox="0 0 58 26"><polygon points="0,0 58,0 29,25" fill="#8bbf3f"/></svg>

  <h2 class="abs heading what-title">What is CBD?</h2>
  <p class="abs what-text">CBD stands for <em>Canna-bi-dy-all</em>. CBD is one of many compounds called phytocan-nabinoids that is found in various plant species. The industrial hemp plant is a plentiful source of CBD. When derived from indus-trial hemp, CBD with less than 0.03% THC by weight has no psychoactive properties but retains all of its positive bio-<br><strong>CBD is commonly used as relief from:</strong></p>
  <ul class="abs uses">
    <li>Pain</li>
    <li>Inflammation</li>
    <li>Anxiety</li>
    <li>Sleep Disorders</li>
    <li>Neurological Disorders</li>
    <li>Opiate Dependence</li>
  </ul>
  <div class="abs sq-lime"></div>
  <div class="abs sq-orange"></div>
  <div class="abs sq-green"></div>

  <div class="abs title-bar"><h1>How Does CBD Work In Your Body?</h1></div>
  <p class="abs intro">Your body produces certain natural compounds called cannabinoids that are used to regulate functions for your entire body. Inside your body there is a processing network for cannabinoids called your Endo-cannabinioid System. CBD mimics the natural cannabinoids produced by your body and stimulates certain receptors found on the surface of cells in your body that effect your ECS. These cells are mainly located in the central nervous system and the immune system. This reaction caused by the in-troduction of CBD helps balance and maintain and restore your body’s natural function. Essentially</p>
  <p class="abs benefits">There are many other benefits from using CBD and hemp products. Hemp products are:</p>
  <div class="abs tag tag-high">High In</div>
  <div class="abs facts facts-high">Omega 3 and 6 Fatty Acids<br>Vitamins A &amp; E<br>Calcium, Iron &amp; Antioxidants</div>
  <div class="abs tag tag-low">Low In</div>
  <div class="abs facts facts-low">Saturated Fats<br>Cholesterol<br>Carbohydrates</div>

  <div class="abs visual" role="img" aria-label="Illustration of a glowing human body with a highlighted brain on a dark molecular background"></div>
  <svg class="abs connectors" width="712" height="477" viewBox="0 0 712 477" fill="none" stroke="#e6e6e6" stroke-width="1">
    <polyline points="216,50 140,50 110,80"/>
    <polyline points="348,115 380,115 408,142 440,142"/>
    <polyline points="216,268 170,268"/>
    <polyline points="348,240 438,240"/>
    <polyline points="348,357 390,357 420,385"/>
  </svg>
  <div class="abs receptor-box">
    <p>CB2 receptors are predominantly found in the immune system.</p>
    <p>CB1 and CB2 receptors are found on the surface of cells in your body that effect your endocannanbinoid system.</p>
    <p>CB2 receptors are responsible for the regulation of inflam-mation which in turn reduces pain.</p>
    <p>CB1 receptors are found primarily in the brain controlling memory process-ing, motor regula-tion, appetite, pain sensation, mood, and sleep.</p>
  </div>

  <div class="abs bottom-bar"></div>
</body>
</html>
```